Website Design for a chemical distribution company

Designer must provide full implementation/coding depending on the platform chosen by the client we'd prefer wordpress type CMS system.

We need a modern and bold website setup for our chemical distribution company. It will need to be like a web store however, no purchases take place on the website only inquiries. So for example the customer can go to a product and click on a button that brings up an inquiry window, they populate that with their information and it sends me an email with the inquiry.

We need it done 3 times pretty much the same but maybe a different colour scheme for each industry. for example on the welcome screen we want 3 icons /pictures ie: plastic, resin, industrial. When the customer clicks on the industry they need it directs them to the specific area that is perhaps on a subdomain or somewhere on the main domain but with no relation to the other industries I hope this makes sense. The layout would be the same but their should be some difference such as colours etc.

The site needs to have a powerful search engine that is very accurate.

It will have about 40,000 products and needs to be able to upload our products via an excel spreed sheet.

We need it to look graphically amazing and very easy to use for the customer.

It will also need to have a blog section that we can upload blogs to daily with different sub categories for things such as experiments, news etc.

The front page needs to be have a banner/advertisement window that is easy for us to change with new specials/deals that we bring out.

Basically the site needs to be easy to navigate, easy to get to products and inquire and needs to have a wow factor.

We also need a special requess page that gives the customers the facility to request a product that they can't find on our website.

I need to stress the importance of a search engine on the site that can handle searching through all the products.

We will also give you the words and you will need to put those on to the pages.

You will also be required to upload our catalogue via CSV or Excel to the site on final completion.

Please find similar websites below for companies that similar to us:

www.tarvelo.com
www.brenti-koval.com
http://www.northumlab.com.au

Just to clarify only one of the websites will have 40-50k products the other 2 industries will only have about 200-500 products each. Added Sunday, February 14, 2016

Reason: Finalising designs and need more time.

Target Market(s)

Chemicals, Food, Pharmaceuticals, Business to Business

Industry/Entity Type

It Company

Coding

Coded - Design and coding required

Number of Pages Required

5+ page

Font styles to use
Sans Serif

Requirements
Must have
• Powerful search engine
• Great design
• Easy to use CMS
• SEO
• Mobile Device Compatible

```html
<!DOCTYPE html>
<html lang="en">
<head>
<meta charset="utf-8">
<title>Corvane — Chemical Distribution</title>
<link href="https://fonts.googleapis.com/css2?family=Open+Sans:wght@400;600;700&family=Raleway:wght@300;400;600;800&display=swap" rel="stylesheet">
<style>
:root{
  --blue:#0a72bd;
  --blue-field:#2a86cb;
  --blue-dark:#07548c;
  --ink:#2b2b2b;
  --muted:#8a8a8a;
  --topbar:#333333;
  --footer:#2d2d2d;
  --footer-line:#474747;
  --offer-bg:#f3f5f7;
  --white:#ffffff;
}
*{margin:0;padding:0;box-sizing:border-box}
html,body{width:850px;height:1200px;overflow:hidden;background:var(--white)}
body{font-family:"Open Sans",Arial,sans-serif;color:var(--ink)}
.page{position:absolute;left:0;top:0;width:1350px;height:1906px;transform:scale(0.62963);transform-origin:0 0}
.abs{position:absolute}

/* top bar */
.topbar{left:0;top:0;width:1350px;height:46px;background:var(--topbar);color:var(--white);font-size:13px}
.topbar .contact{position:absolute;top:15px;display:flex;align-items:center;gap:8px}
.social{position:absolute;top:17px;width:12px;height:12px;border-radius:50%;background:var(--white)}
.social.active{background:#2a9fe0}

/* header */
.brand{left:100px;top:62px;font-size:34px;font-weight:600;color:var(--blue);letter-spacing:0.5px}
.nav{top:79px;font-size:13px;color:var(--ink)}
.nav.current{color:var(--blue);font-weight:700}
.nav-marker{left:802px;top:46px;width:73px;height:3px;background:var(--blue)}

/* hero */
.hero{left:0;top:121px;width:1350px;height:445px;background:linear-gradient(100deg,#f2f6f9 0%,#e3edf3 35%,#d3e4ee 60%,#e6eff4 100%)}
.hero-title{left:100px;top:266px;font-family:"Raleway",sans-serif;font-weight:800;font-size:55px;color:#2a2a2a;letter-spacing:0.5px}
.hero-title span{color:var(--blue)}
.hero-text{left:101px;top:333px;width:520px;font-size:13px;line-height:20px;color:#333}
.btn{display:flex;align-items:center;justify-content:center;font-size:13px;text-transform:uppercase}
.btn-solid{background:var(--blue);color:var(--white)}
.btn-outline{border:1px solid #2b2b2b;color:#2b2b2b;background:transparent}

/* special request */
.request{left:790px;top:185px;width:437px;height:392px;background:var(--blue);color:var(--white)}
.request-title{left:31px;top:18px;font-size:30px;font-weight:600;letter-spacing:0.5px}
.request-rule{top:57px;height:2px;background:var(--white)}
.request-sub{left:31px;top:69px;font-size:13px}
.field{left:27px;width:373px;background:var(--blue-field);color:#cfe4f4;font-size:13px;padding:12px 14px}
.request-submit{left:31px;top:322px;width:373px;height:40px;background:var(--white);color:var(--blue);font-size:13px;letter-spacing:0.5px}

/* categories */
.section-title{font-family:"Raleway",sans-serif;font-weight:400;color:#2a2a2a}
.section-title strong{font-weight:800;color:var(--blue)}
.card{top:659px;width:371px;height:265px;overflow:hidden}
.card-label{left:0;bottom:0;width:100%;height:42px;background:rgba(40,40,40,0.78);color:var(--white);font-weight:600;font-size:15px;display:flex;align-items:center;justify-content:center}
.card-active{background:linear-gradient(160deg,#1a7cc2,#0b6db5 60%,#0a66aa);color:var(--white);text-align:center}

/* offer */
.offer{left:100px;top:959px;width:1150px;height:275px;background:var(--offer-bg)}
.offer-title{left:124px;top:74px;font-family:"Raleway",sans-serif;font-weight:300;font-size:31px;color:#2a2a2a}

/* blog */
.blog-frame{left:100px;top:1338px;width:250px;height:227px;background:var(--blue);padding:10px}
.blog-photo{width:100%;height:100%;background:linear-gradient(135deg,#c7a24a 0%,#8f6d3a 40%,#8d90d4 70%,#6f74c0 100%)}
.dot{top:1524px;width:9px;height:9px;border-radius:50%;background:#222}

/* footer */
.footer{left:0;top:1604px;width:1350px;height:258px;background:var(--footer);color:var(--white)}
.foot-head{top:34px;font-size:13px;font-weight:700}
.foot-text{font-size:13px;line-height:20px;color:#e6e6e6}
.foot-rule{height:1px;background:var(--footer-line)}
.thumb{width:71px;height:71px}
.legal{left:0;top:1862px;width:1350px;height:44px;background:var(--blue);color:var(--white);font-size:13px}
</style>
</head>
<body>
<div class="page">

  <!-- top bar -->
  <div class="abs topbar">
    <div class="contact" style="left:101px">
      <svg width="13" height="13" viewBox="0 0 24 24"><path fill="#fff" d="M6.6 10.8a15.1 15.1 0 0 0 6.6 6.6l2.2-2.2c.3-.3.7-.4 1-.2 1.1.4 2.3.6 3.6.6.6 0 1 .4 1 1V20c0 .6-.4 1-1 1A17 17 0 0 1 3 4c0-.6.4-1 1-1h3.5c.6 0 1 .4 1 1 0 1.3.2 2.5.6 3.6.1.3 0 .7-.2 1z"/></svg>
      <span>(555) 014 772 30</span>
    </div>
    <div class="contact" style="left:242px">
      <svg width="15" height="11" viewBox="0 0 15 11"><rect x="0.5" y="0.5" width="14" height="10" fill="none" stroke="#fff"/><path d="M0.5 0.5l7 5.5 7-5.5" fill="none" stroke="#fff"/></svg>
      <span>info@corvane.com</span>
    </div>
    <div class="social" style="left:1143px"></div>
    <div class="social active" style="left:1175px"></div>
    <div class="social" style="left:1207px"></div>
    <div class="social" style="left:1239px"></div>
  </div>

  <!-- header -->
  <div class="abs brand">corvane</div>
  <div class="abs nav-marker"></div>
  <div class="abs nav current" style="left:818px">HOME</div>
  <div class="abs nav" style="left:887px">ABOUT US</div>
  <div class="abs nav" style="left:978px">WHY CHOOSE US</div>
  <div class="abs nav" style="left:1111px">BLOGS</div>
  <div class="abs nav" style="left:1182px">PRODUCTS</div>

  <!-- hero -->
  <div class="abs hero" role="img" aria-label="Soft, faded laboratory photograph of a scientist handling glassware"></div>
  <svg class="abs" style="left:28px;top:311px" width="44" height="48" viewBox="0 0 44 48"><path d="M22 1 43 13v22L22 47 1 35V13z" fill="none" stroke="#333" stroke-width="1.5"/><path d="M25 18l-6 6 6 6" fill="none" stroke="#333" stroke-width="2"/></svg>
  <svg class="abs" style="left:1278px;top:311px" width="44" height="48" viewBox="0 0 44 48"><path d="M22 1 43 13v22L22 47 1 35V13z" fill="#0a72bd"/><path d="M19 18l6 6-6 6" fill="none" stroke="#fff" stroke-width="2"/></svg>
  <div class="abs hero-title">WELCOME TO <span>CORVANE</span></div>
  <p class="abs hero-text">Lorem ipsum dolor sit amet consectetuer adipiscing elit aenean commodo ligula eget dolor aenean massa cum sociis natoque penatibus et.</p>
  <div class="abs btn btn-solid" style="left:100px;top:393px;width:132px;height:42px">Learn More</div>
  <div class="abs btn btn-outline" style="left:242px;top:393px;width:132px;height:42px">View Products</div>

  <!-- special request -->
  <svg class="abs" style="left:774px;top:566px" width="485" height="12" viewBox="0 0 485 12"><path d="M0 0h16v11z" fill="#07548c"/><path d="M469 0h16l-16 11z" fill="#07548c"/></svg>
  <div class="abs request">
    <div class="abs request-title">SPECIAL REQUEST</div>
    <div class="abs request-rule" style="left:31px;width:231px"></div>
    <div class="abs request-rule" style="left:268px;width:17px"></div>
    <div class="abs request-sub">Request a product which you can't find on our website!</div>
    <div class="abs field" style="top:107px;height:39px">Your Email</div>
    <div class="abs field" style="top:157px;height:39px">Product Name</div>
    <div class="abs field" style="top:207px;height:102px">Description...</div>
    <div class="abs btn request-submit">Submit</div>
  </div>

  <!-- categories -->
  <div class="abs section-title" style="left:0;top:603px;width:1350px;text-align:center;font-size:30px">PRODUCT <strong>CATEGORIES</strong></div>
  <div class="abs card" style="left:100px;background:linear-gradient(180deg,#eef0f2 0%,#dcdfe2 55%,#d88a3a 80%,#4f6b5e 100%)" role="img" aria-label="Laboratory glassware with coloured liquids">
    <div class="abs card-label">PLASTIC</div>
  </div>
  <div class="abs card card-active" style="left:490px" role="img" aria-label="Blue-tinted photo of poured resin">
    <div class="abs" style="left:0;top:73px;width:100%;font-size:15px;font-weight:600">RESIN</div>
    <div class="abs" style="left:55px;top:103px;width:261px;font-size:13px;line-height:20px">Nulla consequat massa quis enim donec pede justo fringilla vel.</div>
    <svg class="abs" style="left:164px;top:165px" width="42" height="42" viewBox="0 0 42 42"><circle cx="21" cy="21" r="21" fill="#fff"/><circle cx="19.5" cy="19.5" r="4" fill="none" stroke="#0a72bd" stroke-width="1.8"/><path d="M22.5 22.5l4 4" stroke="#0a72bd" stroke-width="2"/></svg>
  </div>
  <div class="abs card" style="left:880px;background:linear-gradient(180deg,#4f8fcc 0%,#8fb4d6 45%,#7a5b45 70%,#5b4a3d 100%)" role="img" aria-label="Industrial plant with rusted pipework under a blue sky">
    <div class="abs card-label">INDUSTRIAL</div>
  </div>

  <!-- offer -->
  <div class="abs offer">
    <div class="abs offer-title">Special Offer Advertisment</div>
    <div class="abs btn btn-solid" style="left:224px;top:131px;width:150px;height:47px;font-size:12px">View Deal</div>
    <div class="abs" style="left:680px;top:36px;width:325px;height:239px;background:radial-gradient(ellipse at 55% 75%,#3aa3e6 0%,#7cc6ef 45%,rgba(243,245,247,0) 75%)" role="img" aria-label="Two blue flasks joined by a looping glass tube"></div>
  </div>

  <!-- blog -->
  <div class="abs section-title" style="left:100px;top:1270px;font-size:36px">BLOG <strong>POSTS</strong></div>
  <div class="abs blog-frame"><div class="blog-photo" role="img" aria-label="Gloved hands holding a small vial of amber liquid"></div></div>
  <div class="abs" style="left:419px;top:1348px;font-size:15px;color:var(--muted)">Thursday</div>
  <div class="abs" style="left:410px;top:1358px;font-family:Raleway,sans-serif;font-size:76px;line-height:80px;color:#8c8c8c">10</div>
  <div class="abs" style="left:508px;top:1356px;font-size:19px;line-height:25px;color:#2a2a2a">Lorem Ipsum is simply<br>dummy text</div>
  <div class="abs" style="left:510px;top:1409px;font-size:16px;color:var(--muted)">Sydney,Australia</div>
  <p class="abs" style="left:423px;top:1444px;width:815px;font-size:13px;line-height:22px;color:var(--muted)">Lorem Ipsum is simply dummy text of the printing and typesetting industry. Lorem Ipsum has been the industry's standard dummy text ever since the 1500s, when an unknown printer took a galley of type and scrambled it to make a type specimen book. It has survived not only five centuries.</p>
  <div class="abs dot" style="left:424px"></div>
  <div class="abs dot" style="left:436px;background:var(--blue)"></div>
  <div class="abs dot" style="left:448px"></div>

  <!-- footer -->
  <div class="abs footer">
    <div class="abs foot-head" style="left:100px">CONTACT INFO</div>
    <div class="abs foot-text" style="left:101px;top:56px;font-weight:700">ADDRESS:</div>
    <div class="abs foot-text" style="left:179px;top:56px">01 Lorem Street, Dummy,<br>Ipsum, Country</div>
    <div class="abs foot-rule" style="left:101px;top:107px;width:231px"></div>
    <div class="abs foot-text" style="left:101px;top:123px;font-weight:700">PHONE:</div>
    <div class="abs foot-text" style="left:179px;top:123px">(555) 014 772 30<br>(555) 019 338 61</div>
    <div class="abs foot-rule" style="left:101px;top:174px;width:231px"></div>
    <div class="abs foot-text" style="left:101px;top:190px;font-weight:700">EMAIL:</div>
    <div class="abs foot-text" style="left:179px;top:190px">info@corvane.com</div>
    <div class="abs foot-rule" style="left:101px;top:225px;width:231px"></div>

    <div class="abs foot-head" style="left:408px">LATEST PRODUCTS</div>
    <div class="abs thumb" style="left:408px;top:62px;background:linear-gradient(135deg,#1d1d1d,#7a6a55)" role="img" aria-label="Microscope close-up"></div>
    <div class="abs thumb" style="left:488px;top:62px;background:linear-gradient(135deg,#e9e6e0,#c98b6a)" role="img" aria-label="Hand holding a test tube"></div>
    <div class="abs thumb" style="left:568px;top:62px;background:linear-gradient(135deg,#c9c3c9,#d5669a)" role="img" aria-label="Sample tubes in a rack"></div>
    <div class="abs thumb" style="left:408px;top:142px;background:linear-gradient(135deg,#3a5f7a,#d08a3a)" role="img" aria-label="Laboratory instrument"></div>
    <div class="abs thumb" style="left:488px;top:142px;background:linear-gradient(135deg,#3a3a3a,#c4b79a)" role="img" aria-label="Lit analysis equipment"></div>
    <div class="abs thumb" style="left:568px;top:142px;background:linear-gradient(135deg,#a9e03a,#5fa83a)" role="img" aria-label="Green liquid vials"></div>

    <div class="abs foot-head" style="left:714px">RECENT POSTS</div>
    <div class="abs foot-text" style="left:712px;top:56px"><b>LOREM IPSUM DOLOR SIT EMIT EN.</b><br>Feb 15, 2016 / By Admin / 7 Comments</div>
    <div class="abs foot-rule" style="left:712px;top:106px;width:231px"></div>
    <div class="abs foot-text" style="left:712px;top:118px"><b>LOREM IPSUM DOLOR SIT EMIT EN.</b><br>Feb 15, 2016 / By Admin / 7 Comments</div>
    <div class="abs foot-rule" style="left:712px;top:167px;width:231px"></div>
    <div class="abs foot-text" style="left:712px;top:179px"><b>LOREM IPSUM DOLOR SIT EMIT EN.</b><br>Feb 15, 2016 / By Admin / 7 Comments</div>
    <div class="abs foot-rule" style="left:712px;top:229px;width:231px"></div>

    <div class="abs foot-head" style="left:1020px">NEWSLETTER SIGNUP</div>
    <div class="abs foot-text" style="left:1019px;top:56px">Enter your email address to subscribe<br>and receive notification.</div>
    <div class="abs" style="left:1019px;top:113px;width:231px;height:33px;border:1px solid #5a5a5a;color:#8a8a8a;font-size:13px;padding:7px 16px">Email Address</div>
    <div class="abs btn" style="left:1019px;top:154px;width:231px;height:33px;background:#1b1b1b;color:#fff">Submit</div>
  </div>

  <div class="abs legal">
    <div class="abs" style="left:100px;top:14px">© 2016 CORVANE, ALL RIGHTS RESERVED</div>
    <div class="abs" style="left:981px;top:14px">PRIVACY POLICY &nbsp;&nbsp; | &nbsp;&nbsp; TERMS &amp; CONDITIONS</div>
  </div>

</div>
</body>
</html>
```